Marketing Thornbury

We are a primary school and would like to market our school in a positive light. We have had recent success and would like the local community to know!

Target Market(s)

Parents/Carers in the local community

Industry/Entity Type

School

Font styles to use
Serif

Requirements
Must have
• Thornbury Logo first with our moto 'Opening Minds Side by Side'

Reference to the fact we are converting to academy status on 1st April 2014 with The Harrowby BRIDGE Academy Trust

Reference to the partnership with Caldwick Primary School which has bought recent, quick success

Reference to Edvisor rating of Good. Feb 2014
Nice to have
• School colours dark red

Link to website www.thornburyprimary.example

Link to the academy website www.harrowbybridge.example

Statements from Edvisor -

'This is a good school'

'The Executive Headteacher and leadership team have skilfully steered the school's recovery and galvanised staff at all levels to work as a team'

'This is a very different school to the one that existed at the time of the previous inspection'

'Pupils achievement has improved very quickly this year'

'Pupils make a strong start in the school'

'The quality of teaching is good'

'The behaviour of pupils is good'

```html
<!DOCTYPE html>
<html lang="en">
<head>
<meta charset="utf-8">
<title>Thornbury School – Opening Minds Side by Side</title>
<link rel="stylesheet" href="https://fonts.googleapis.com/css2?family=PT+Serif:wght@400;700&display=swap">
<style>
  :root {
    --maroon: #7a1a22;
    --maroon-deep: #5e1118;
    --gold: #f6b918;
    --text-yellow: #f7c21a;
    --slate: #34384a;
    --ink: #1a1a1a;
    --white: #ffffff;
    --pill-top: #e4e4e4;
    --pill-bottom: #a9a9a9;
    --leaf: #8aa53a;
    --photo-a: #c9b8a6;
    --photo-b: #8c8f9c;
    --serif: "PT Serif", Georgia, serif;
  }
  * { margin: 0; padding: 0; box-sizing: border-box; }
  html, body { width: 947px; height: 1200px; overflow: hidden; background: var(--maroon); }
  .flyer { position: relative; width: 947px; height: 1200px; background: var(--maroon); overflow: hidden; font-family: var(--serif); }

  .header-band { position: absolute; left: 0; top: 0; width: 947px; height: 240px; background: var(--gold); }
  .headline {
    position: absolute; left: 0; width: 100%; top: 40px; text-align: center;
    font-weight: 700; font-size: 56px; line-height: 70px; color: var(--ink);
  }
  .subhead {
    position: absolute; left: 0; width: 100%; top: 125px; padding-left: 48px; text-align: center;
    font-weight: 700; font-size: 34px; line-height: 44px; color: var(--slate);
  }

  .photo-band { position: absolute; left: 0; top: 0; width: 947px; height: 700px; }

  .school-mark {
    position: absolute; left: 46px; top: 598px; width: 224px; height: 215px;
    background: var(--white); padding: 10px;
  }
  .school-mark-inner {
    width: 100%; height: 100%; background: var(--maroon-deep);
    display: flex; flex-direction: column; align-items: center; justify-content: center; gap: 14px;
  }
  .school-mark-dot { width: 70px; height: 70px; border-radius: 50%; background: var(--gold); }
  .school-mark-name {
    font-weight: 700; font-size: 22px; color: var(--gold); letter-spacing: 1px; text-align: center; line-height: 1.15;
  }

  .partnership-note {
    position: absolute; left: 50px; top: 826px; width: 420px;
    font-weight: 700; font-size: 22px; line-height: 32px; color: var(--text-yellow);
  }

  .inspection-points { position: absolute; left: 48px; top: 950px; width: 440px; list-style: none; }
  .inspection-points li {
    position: relative; padding-left: 34px; margin-bottom: 9px;
    font-size: 15px; line-height: 20px; color: var(--white);
  }
  .inspection-points svg { position: absolute; left: 0; top: 1px; width: 18px; height: 18px; }

  .academy-note {
    position: absolute; left: 520px; width: 350px; top: 668px; text-align: center;
    font-weight: 700; font-size: 26px; line-height: 38px; color: var(--text-yellow);
  }

  .trust-mark {
    position: absolute; left: 545px; top: 880px; width: 297px; height: 93px;
    background: var(--white); display: flex; align-items: center; justify-content: center; gap: 14px;
  }
  .trust-mark-square { width: 40px; height: 40px; background: var(--leaf); flex: none; }
  .trust-mark-name { font-weight: 400; font-size: 18px; line-height: 23px; color: var(--slate); letter-spacing: 0.5px; }

  .web-links {
    position: absolute; left: 515px; width: 380px; top: 1000px; text-align: center;
    font-weight: 700; font-size: 22px; line-height: 40px; color: var(--white);
  }

  .verdict-pill {
    position: absolute; left: 548px; top: 1117px; width: 327px; height: 42px; border-radius: 8px;
    background: linear-gradient(var(--pill-top), var(--pill-bottom));
    font-weight: 700; font-size: 26px; line-height: 42px; text-align: center; color: var(--ink);
  }
</style>
</head>
<body>
<main class="flyer">
  <div class="header-band"></div>
  <h1 class="headline">Opening Minds Side by Side</h1>
  <h2 class="subhead">The Quality of Teaching is Good</h2>

  <svg class="photo-band" viewBox="0 0 947 700" role="img" aria-label="Photograph of six smiling pupils in white shirts and striped ties standing together in the school library">
    <defs>
      <linearGradient id="photoTone" x1="0" y1="0" x2="1" y2="1">
        <stop offset="0" stop-color="var(--photo-a)"/>
        <stop offset="0.55" stop-color="#e6ddd4"/>
        <stop offset="1" stop-color="var(--photo-b)"/>
      </linearGradient>
    </defs>
    <polygon points="0,230 250,230 285,212 640,212 668,198 947,198 947,646 862,646 840,628 430,628 405,654 0,654"
             fill="url(#photoTone)" stroke="var(--white)" stroke-width="5" stroke-linejoin="round"/>
  </svg>

  <div class="school-mark">
    <div class="school-mark-inner">
      <span class="school-mark-dot"></span>
      <span class="school-mark-name">THORNBURY<br>SCHOOL</span>
    </div>
  </div>

  <p class="partnership-note">In partnership with<br>Caldwick Primary School</p>

  <ul class="inspection-points">
    <li><svg viewBox="0 0 18 18"><circle cx="9" cy="9" r="9" fill="var(--gold)"/><path d="M4.5 9.2l3 3 6-6.2" fill="none" stroke="var(--maroon)" stroke-width="2.2"/></svg>Pupils achievement has improved very quickly this year'</li>
    <li><svg viewBox="0 0 18 18"><circle cx="9" cy="9" r="9" fill="var(--gold)"/><path d="M4.5 9.2l3 3 6-6.2" fill="none" stroke="var(--maroon)" stroke-width="2.2"/></svg>Pupils make a strong start in the school</li>
    <li><svg viewBox="0 0 18 18"><circle cx="9" cy="9" r="9" fill="var(--gold)"/><path d="M4.5 9.2l3 3 6-6.2" fill="none" stroke="var(--maroon)" stroke-width="2.2"/></svg>The behaviour of pupils is good</li>
    <li><svg viewBox="0 0 18 18"><circle cx="9" cy="9" r="9" fill="var(--gold)"/><path d="M4.5 9.2l3 3 6-6.2" fill="none" stroke="var(--maroon)" stroke-width="2.2"/></svg>Reference to Edvisor rating of Good. Feb 2014</li>
    <li><svg viewBox="0 0 18 18"><circle cx="9" cy="9" r="9" fill="var(--gold)"/><path d="M4.5 9.2l3 3 6-6.2" fill="none" stroke="var(--maroon)" stroke-width="2.2"/></svg>This is a very different school to the one that existed at the time of the previous inspection</li>
    <li><svg viewBox="0 0 18 18"><circle cx="9" cy="9" r="9" fill="var(--gold)"/><path d="M4.5 9.2l3 3 6-6.2" fill="none" stroke="var(--maroon)" stroke-width="2.2"/></svg>The Executive Headteacher and leadership team have skilfully steered the school's recovery and galvanised staff at all levels to work as a team</li>
  </ul>

  <p class="academy-note">Reference to the fact we are converting to academy status on 1st April 2014 with The Harrowby BRIDGE Academy Trust</p>

  <div class="trust-mark">
    <span class="trust-mark-square"></span>
    <span class="trust-mark-name">HARROWBY BRIDGE<br>ACADEMY TRUST</span>
  </div>

  <p class="web-links">www.harrowbybridge.example<br>www.thornburyprimary.example</p>

  <div class="verdict-pill">This is a Good School</div>
</main>
</body>
</html>
```